Personal contact Business card design needed

I work in the Property Industry - specifically Property Management.

I need a card I can hand out to colleagues at networking events, meetings, training courses etc. that will provide my contact details.

Target Market(s)

Professional colleagues / potential clients / employers

Industry/Entity Type

Training

Contact Information for Business Card

I need a simple and professional card to give to professional network contacts at meetings, interviews etc.

The card should include my photograph, name, mobile number, email address and Proflinx address.

I would like appropriate professional colours. Something feminine but not too 'frilly' or 'girly'

Requirements
Must have
• Photograph of myself.
I want it to be simple,perhaps a small icon for each contact detail such as
Email icon
Proflinx icon
Mobile number

```html
<!DOCTYPE html>
<html lang="en">
<head>
<meta charset="utf-8">
<title>Jane Doe – Business Card</title>
<link rel="stylesheet" href="https://fonts.googleapis.com/css2?family=Josefin+Sans:wght@300;400&display=swap">
<style>
  :root {
    --berry: #9a1c50;
    --berry-deep: #821543;
    --paper: #ffffff;
    --backdrop: #e6e4e1;
    --photo-light: #bdbdbd;
    --photo-dark: #3a3a3a;
  }
  * { box-sizing: border-box; margin: 0; padding: 0; }
  html, body {
    width: 1200px;
    height: 900px;
    overflow: hidden;
    background: var(--backdrop);
  }
  body {
    display: flex;
    align-items: center;
    justify-content: center;
    font-family: "Josefin Sans", "Helvetica Neue", Arial, sans-serif;
  }
  .business-card {
    position: relative;
    width: 960px;
    height: 548px;
    overflow: hidden;
    box-shadow: 0 10px 30px rgba(0,0,0,0.18);
  }
  .card-background {
    position: absolute;
    inset: 0;
    width: 100%;
    height: 100%;
  }
  .portrait-frame {
    position: absolute;
    left: 157px;
    top: 210px;
    width: 176px;
    height: 176px;
    border-radius: 50%;
    background: var(--paper);
    padding: 9px;
    box-shadow: 0 3px 8px rgba(0,0,0,0.25);
  }
  .portrait {
    width: 100%;
    height: 100%;
    border-radius: 50%;
    background: radial-gradient(circle at 50% 45%, var(--photo-light) 0%, #8c8c8c 55%, var(--photo-dark) 100%);
  }
  .holder-name {
    position: absolute;
    left: 95px;
    top: 400px;
    width: 300px;
    text-align: center;
    color: var(--paper);
    font-weight: 300;
    font-size: 54px;
    letter-spacing: 0.5px;
  }
  .contact-list {
    position: absolute;
    left: 438px;
    top: 120px;
    list-style: none;
  }
  .contact-item {
    display: flex;
    align-items: center;
    height: 46px;
    margin-bottom: 22px;
  }
  .contact-icon {
    flex: none;
    width: 46px;
    height: 46px;
    border-radius: 50%;
    background: var(--berry);
    display: flex;
    align-items: center;
    justify-content: center;
    color: var(--paper);
    font-size: 26px;
    font-weight: 400;
    box-shadow: 0 2px 4px rgba(0,0,0,0.2);
  }
  .contact-icon svg { width: 24px; height: 24px; fill: var(--paper); }
  .contact-text {
    margin-left: 20px;
    color: var(--berry);
    font-size: 21px;
    font-weight: 300;
    letter-spacing: 0.2px;
    white-space: nowrap;
  }
</style>
</head>
<body>
  <article class="business-card">
    <svg class="card-background" viewBox="0 0 960 548" aria-hidden="true">
      <defs>
        <linearGradient id="berry-fill" x1="0" y1="0" x2="0" y2="1">
          <stop offset="0" stop-color="#9a1c50"/>
          <stop offset="1" stop-color="#821543"/>
        </linearGradient>
        <filter id="curve-shadow" x="-20%" y="-20%" width="140%" height="140%">
          <feDropShadow dx="-3" dy="3" stdDeviation="4" flood-opacity="0.25"/>
        </filter>
      </defs>
      <rect width="960" height="548" fill="url(#berry-fill)"/>
      <circle cx="762" cy="220" r="343" fill="#ffffff" filter="url(#curve-shadow)"/>
      <rect x="762" y="0" width="198" height="548" fill="#ffffff"/>
    </svg>

    <div class="portrait-frame">
      <div class="portrait" role="img" aria-label="Portrait photograph of Jane Doe"></div>
    </div>
    <h1 class="holder-name">Jane Doe</h1>

    <ul class="contact-list">
      <li class="contact-item">
        <span class="contact-icon">
          <svg viewBox="0 0 24 24" aria-hidden="true"><path d="M6.6 10.8c1.4 2.8 3.8 5.1 6.6 6.6l2.2-2.2c.3-.3.7-.4 1-.2 1.1.4 2.3.6 3.6.6.6 0 1 .4 1 1V20c0 .6-.4 1-1 1C10.6 21 3 13.4 3 4c0-.6.4-1 1-1h3.5c.6 0 1 .4 1 1 0 1.3.2 2.5.6 3.6.1.3 0 .7-.2 1z"/></svg>
        </span>
        <span class="contact-text">0201478352</span>
      </li>
      <li class="contact-item">
        <span class="contact-icon">@</span>
        <span class="contact-text">samplemail@mailnest.com</span>
      </li>
      <li class="contact-item">
        <span class="contact-icon" aria-hidden="true"></span>
        <span class="contact-text">proflinx.com/member/jdoe-property/5208</span>
      </li>
    </ul>
  </article>
</body>
</html>
```